Need Web Design for Business Process Outsourcing Company (Kelmora)

Kelmora is a business process outsourcing company. Need a simple site similar to http://www.tarvenholm.com/ but with a more professional and credible look. New to the process; not sure where to start and comparing my options. Please let me know what my options are if I choose to go with you. Logo is attached for your reference. Please use same colorway

Reason: I want the final product to be coded. Please confirm you will be able to code final design.

Industry/Entity Type

Business

Coding

Coded - Design and coding required

```html
<!DOCTYPE html>
<html lang="en">
<head>
<meta charset="utf-8">
<title>Kelmora Services</title>
<link rel="stylesheet" href="https://fonts.googleapis.com/css2?family=Montserrat:wght@400;600;700&family=Arimo:wght@400;700&display=swap">
<style>
:root{
  --blue:#0b86c6;
  --blue-dark:#0a5a92;
  --navy:#0d4f7f;
  --ink:#222;
  --body:#555;
  --pale:#e7f2fa;
  --grey-bg:#f4f4f4;
  --line:#c9c9c9;
  --white:#fff;
}
*{margin:0;padding:0;box-sizing:border-box}
html,body{width:1200px;height:2752px;overflow:hidden;background:var(--white)}
body{position:relative;font-family:"Arimo",Arial,sans-serif;color:var(--body)}
.abs{position:absolute}
.heading{font-family:"Montserrat",Arial,sans-serif}

/* header / hero */
.hero-photo{left:0;top:0;width:1200px;height:660px;background:linear-gradient(135deg,#1d2329 0%,#3a434c 40%,#6c757d 62%,#2b3238 100%)}
.wave{left:0;top:480px;width:1200px;height:390px}
.brand{left:77px;top:14px;display:flex;align-items:center;gap:12px}
.brand-mark{width:44px;height:44px;background:var(--blue)}
.brand-name{font-family:"Montserrat",sans-serif;font-weight:700;font-size:34px;color:var(--white)}
.nav{right:80px;top:30px;display:flex;gap:28px;font-family:"Montserrat",sans-serif;font-size:15px;color:var(--white)}
.nav .active{color:var(--blue)}
.hero-title{left:77px;top:235px;color:var(--white);font-family:"Montserrat",sans-serif;line-height:1}
.hero-title .small{font-size:82px;font-weight:400;display:block}
.hero-title .big{font-size:100px;font-weight:400;display:block;margin-top:8px}
.btn-quote{left:77px;top:433px;width:230px;height:51px;background:var(--blue);color:var(--white);font-family:"Montserrat",sans-serif;font-size:19px;display:flex;align-items:center;justify-content:center}

/* services */
.services-title{left:0;width:1200px;top:725px;text-align:center;color:var(--white);font-family:"Montserrat",sans-serif;font-size:40px}
.services-title b{font-weight:700}
.service{top:800px;width:220px;text-align:center}
.service .ring{width:156px;height:156px;margin:0 auto;border-radius:50%;background:#e9eef2;display:flex;align-items:center;justify-content:center}
.service .disc{width:124px;height:124px;border-radius:50%;background:var(--white);display:flex;align-items:center;justify-content:center;box-shadow:0 2px 6px rgba(0,0,0,.12)}
.service h3{margin-top:12px;font-family:"Montserrat",sans-serif;font-weight:400;font-size:19px;color:var(--ink);letter-spacing:.3px}
.service p{margin-top:10px;font-size:15px;line-height:23px;color:var(--body)}

/* global presence */
.presence{left:0;top:1116px;width:1200px;height:334px;background:var(--pale)}
.presence h2{left:79px;top:48px;font-family:"Montserrat",sans-serif;font-weight:400;font-size:33px;color:var(--blue)}
.presence p{left:79px;top:104px;width:540px;font-size:14.5px;line-height:23px}
.btn-outline{border:1.5px solid var(--navy);color:var(--navy);font-family:"Montserrat",sans-serif;font-size:15px;display:flex;align-items:center;justify-content:center;background:var(--white)}
.presence .btn-outline{left:77px;top:229px;width:146px;height:51px;background:transparent}
.world-map{left:679px;top:58px;width:440px;height:222px;border-radius:40px;background:radial-gradient(ellipse at 45% 50%,#7c7c7c 0%,#8d8d8d 55%,var(--pale) 75%)}

/* engage */
.engage h2{left:0;width:1200px;top:1498px;text-align:center;font-family:"Montserrat",sans-serif;font-weight:400;font-size:31px;color:var(--blue)}
.engage p{left:160px;width:880px;top:1553px;text-align:center;font-size:14.5px;line-height:23px}
.engage .btn-outline{left:517px;top:1637px;width:166px;height:51px}

/* blog */
.blog{left:0;top:1740px;width:1200px;height:334px;background:var(--grey-bg)}
.section-title{left:0;width:1200px;text-align:center;font-family:"Montserrat",sans-serif;font-weight:400;font-size:40px;color:var(--ink)}
.section-title b{color:var(--navy);font-weight:700}
.post-photo{width:148px;height:148px;border-radius:50%;border:3px solid var(--blue)}
.post-date{width:60px;height:60px;border-radius:50%;background:var(--blue);color:var(--white);font-family:"Montserrat",sans-serif;font-weight:700;font-size:17px;display:flex;align-items:center;justify-content:center}
.post-title{font-family:"Arimo",sans-serif;font-weight:700;font-size:19px;color:var(--ink)}
.post-text{width:300px;font-size:14.5px;line-height:23px}
.blog .btn-outline{width:144px;height:51px}

/* contact */
.field{border:1.5px solid var(--line);background:var(--white);font-size:14px;color:#999;padding:10px 16px}
.btn-submit{left:527px;top:2341px;width:146px;height:50px;background:var(--navy);color:var(--white);font-family:"Montserrat",sans-serif;font-weight:600;font-size:19px;display:flex;align-items:center;justify-content:center}

/* footer */
.footer{left:0;top:2444px;width:1200px;height:308px;background:linear-gradient(180deg,#1490d0 0%,#0b7fc0 100%);color:var(--white)}
.footer h4{font-family:"Montserrat",sans-serif;font-weight:600;font-size:23px;letter-spacing:.5px}
.contact-list{left:79px;top:86px;font-size:14.5px;line-height:22px}
.contact-list li{list-style:none;display:flex;gap:14px;margin-bottom:12px}
.contact-list svg{flex:none;margin-top:3px}
.foot-brand{left:0;width:1200px;top:48px;display:flex;justify-content:center;align-items:center;gap:10px}
.foot-brand .brand-mark{width:34px;height:34px;background:var(--white)}
.foot-brand .brand-name{font-size:28px}
.foot-text{left:430px;width:340px;top:108px;text-align:center;font-size:14.5px;line-height:23px}
.socials{left:0;width:1200px;top:188px;display:flex;justify-content:center;gap:9px}
.socials span{width:40px;height:40px;border-radius:50%;border:1.5px solid rgba(255,255,255,.6)}
.socials span.on{background:var(--white);border-color:var(--white)}
.links{right:79px;top:86px;text-align:right;font-size:14.5px;line-height:31px;list-style:none}
.copyright{left:0;top:253px;width:1200px;height:55px;background:rgba(0,40,90,.35);display:flex;align-items:center;justify-content:center;font-family:"Montserrat",sans-serif;font-size:15px}
.copyright i{font-weight:700}
</style>
</head>
<body>

<!-- hero -->
<div class="abs hero-photo" role="img" aria-label="Businessman in a suit touching a glowing hexagon interface labelled with service keywords"></div>
<svg class="abs wave" viewBox="0 0 1200 390" aria-hidden="true">
  <defs>
    <linearGradient id="band" x1="0" y1="0" x2="0" y2="1">
      <stop offset="0" stop-color="#0b8bd0"/>
      <stop offset="1" stop-color="#0a5a98"/>
    </linearGradient>
  </defs>
  <path d="M0 125 C350 190 800 140 1200 30 L1200 390 L0 390 Z" fill="url(#band)"/>
  <path d="M0 125 C350 190 800 140 1200 30" fill="none" stroke="#fff" stroke-width="7"/>
  <rect x="0" y="384" width="1200" height="6" fill="#fff"/>
</svg>

<div class="abs brand"><span class="brand-mark"></span><span class="brand-name">Kelmora</span></div>
<nav class="abs nav"><span class="active">HOME</span><span>ABOUT</span><span>SERVICES</span><span>STRATEGY</span><span>EXPERIENCE</span><span>SECURITY</span><span>NEWS</span><span>CONTACT</span></nav>

<h1 class="abs hero-title"><span class="small">We Offer</span><span class="big">SOLUTIONS</span></h1>
<div class="abs btn-quote">GET A FREE QUOTE</div>

<!-- services -->
<h2 class="abs services-title"><b>Kelmora</b> Services</h2>

<div class="abs service" style="left:68px">
  <div class="ring"><div class="disc">
    <svg width="56" height="56" viewBox="0 0 56 56" fill="none" stroke="#0a4f7e" stroke-width="2.2"><circle cx="28" cy="26" r="13"/><path d="M12 28v-4a16 16 0 0 1 32 0v4"/><rect x="9" y="24" width="6" height="10" rx="2"/><rect x="41" y="24" width="6" height="10" rx="2"/><path d="M44 34c0 8-6 11-12 11"/><path d="M14 54c2-8 8-11 14-11s12 3 14 11"/></svg>
  </div></div>
  <h3>CUSTOMER SERVICE</h3>
  <p>Lorem Ipsum is simply dummy text of the printing and typesetting industry.</p>
</div>
<div class="abs service" style="left:279px">
  <div class="ring"><div class="disc">
    <svg width="60" height="56" viewBox="0 0 60 56" fill="none" stroke="#0a4f7e" stroke-width="2.4"><path d="M3 6h9l7 30h32l5-20H15"/><path d="M19 36l-3 8h36"/><circle cx="22" cy="50" r="3.5" stroke="#0b86c6"/><circle cx="46" cy="50" r="3.5" stroke="#0b86c6"/></svg>
  </div></div>
  <h3>ECOMMERCE</h3>
  <p>Lorem Ipsum is simply dummy text of the printing and typesetting industry.</p>
</div>
<div class="abs service" style="left:490px">
  <div class="ring"><div class="disc">
    <svg width="56" height="56" viewBox="0 0 56 56" fill="none" stroke="#0a4f7e" stroke-width="2.2"><path d="M28 12a12 12 0 0 0-7 22v6h14v-6a12 12 0 0 0-7-22z"/><path d="M22 44h12M24 48h8"/><path d="M28 2v5M10 10l4 4M46 10l-4 4M4 26h5M47 26h5" stroke="#0b86c6"/></svg>
  </div></div>
  <h3>CREATIVE</h3>
  <p>Lorem Ipsum is simply dummy text of the printing and typesetting industry.</p>
</div>
<div class="abs service" style="left:701px">
  <div class="ring"><div class="disc">
    <svg width="60" height="56" viewBox="0 0 60 56" fill="none" stroke="#0a4f7e" stroke-width="2.4"><rect x="4" y="8" width="52" height="32" rx="2"/><path d="M30 40v8M18 50h24"/><circle cx="24" cy="24" r="6" stroke="#0b86c6"/><circle cx="37" cy="22" r="4" stroke="#0b86c6"/></svg>
  </div></div>
  <h3>IT SOLUTIONS</h3>
  <p>Lorem Ipsum is simply dummy text of the printing and typesetting industry.</p>
</div>
<div class="abs service" style="left:912px">
  <div class="ring"><div class="disc">
    <svg width="56" height="56" viewBox="0 0 56 56" fill="none" stroke="#0a4f7e" stroke-width="2.2"><circle cx="26" cy="22" r="15"/><circle cx="26" cy="18" r="5"/><path d="M17 31c2-5 5-7 9-7s7 2 9 7"/><path d="M37 33l12 12" stroke-width="4"/><path d="M8 54c2-6 6-9 10-10M44 54c-1-3-2-5-4-6"/></svg>
  </div></div>
  <h3>HUMAN RESOURCES</h3>
  <p>Lorem Ipsum is simply dummy text of the printing and typesetting industry.</p>
</div>

<!-- global presence -->
<section class="abs presence">
  <h2 class="abs">Global Presence</h2>
  <p class="abs">Lorem Ipsum is simply dummy text of the printing and typesetting industry. Lorem Ipsum has been the industry's standard dummy text ever since the 1500s, when an unknown printer took a galley of type and scrambled it to make a type specimen book. It has survived not only five centuries, but also the leap into electronic typesetting, remaining essentially unchanged.</p>
  <div class="abs btn-outline">READ MORE</div>
  <div class="abs world-map" role="img" aria-label="Grey world map with target markers on office locations"></div>
</section>

<!-- engage -->
<section class="engage">
  <h2 class="abs">Passionate about engaging with clients &amp; growing business?</h2>
  <p class="abs">Lorem Ipsum is simply dummy text of the printing and typesetting industry. Lorem Ipsum has been the industry's standard dummy text ever since the 1500s, when an unknown printer took a galley of type and scrambled it to make a type specimen book. It has survived not only five centuries, but also the leap into electronic typesetting, remaining essentially unchanged.</p>
  <div class="abs btn-outline">APPLY WITH US!</div>
</section>

<!-- blog -->
<section class="abs blog">
  <h2 class="abs section-title" style="top:50px">Latest <b>Blog</b></h2>

  <div class="abs post-photo" role="img" aria-label="Business team reviewing documents" style="left:91px;top:124px;background:linear-gradient(135deg,#c8d6e4,#6f7f90 55%,#2c3440)"></div>
  <div class="abs post-date" style="left:73px;top:122px">6.4.16</div>
  <div class="abs post-title" style="left:262px;top:124px">Lorem ipsum is simply</div>
  <div class="abs post-text" style="left:262px;top:158px">Lorem Ipsum is simply dummy text of the printing and typesetting industry.</div>
  <div class="abs btn-outline" style="left:261px;top:216px">READ MORE</div>

  <div class="abs post-photo" role="img" aria-label="Laptops and devices on a desk" style="left:642px;top:124px;background:linear-gradient(135deg,#f2f4f7,#c9cfd8 55%,#7b6f9a)"></div>
  <div class="abs post-date" style="left:624px;top:122px">6.4.16</div>
  <div class="abs post-title" style="left:815px;top:124px">Lorem ipsum is simply</div>
  <div class="abs post-text" style="left:815px;top:158px">Lorem Ipsum is simply dummy text of the printing and typesetting industry.</div>
  <div class="abs btn-outline" style="left:812px;top:216px">READ MORE</div>
</section>

<!-- contact -->
<h2 class="abs section-title" style="top:2120px">Contact <b>US</b></h2>
<div class="abs field" style="left:233px;top:2189px;width:312px;height:42px">Name:</div>
<div class="abs field" style="left:233px;top:2236px;width:312px;height:42px">Phone:</div>
<div class="abs field" style="left:233px;top:2283px;width:312px;height:42px">E-Mail:</div>
<div class="abs field" style="left:550px;top:2189px;width:417px;height:136px">Message:</div>
<div class="abs btn-submit">SUBMIT</div>

<!-- footer -->
<footer class="abs footer">
  <h4 class="abs" style="left:79px;top:30px">CONTACT ADDRESS</h4>
  <ul class="abs contact-list">
    <li><svg width="16" height="20" viewBox="0 0 16 20" fill="#fff"><path d="M8 0a7 7 0 0 0-7 7c0 5 7 13 7 13s7-8 7-13a7 7 0 0 0-7-7zm0 10a3 3 0 1 1 0-6 3 3 0 0 1 0 6z"/></svg><span>123 Building Name, Street,<br>City, Country - Zipcode</span></li>
    <li><svg width="16" height="16" viewBox="0 0 16 16" fill="#fff"><path d="M3 0l3 4-2 2c1 2 4 5 6 6l2-2 4 3-2 3C7 16 0 9 0 3z"/></svg><span>123-4567-890</span></li>
    <li><svg width="16" height="16" viewBox="0 0 16 16" fill="#fff"><rect x="0" y="3" width="4" height="13" rx="1"/><rect x="5" y="5" width="11" height="11" rx="1"/><rect x="7" y="0" width="7" height="4"/></svg><span>123-4567-890</span></li>
    <li><svg width="18" height="14" viewBox="0 0 18 14" fill="#fff"><path d="M0 0h18v2L9 8 0 2z"/><path d="M0 4l9 6 9-6v10H0z"/></svg><span>info@kelmoraservices.com</span></li>
  </ul>

  <div class="abs foot-brand"><span class="brand-mark"></span><span class="brand-name">Kelmora</span></div>
  <p class="abs foot-text">Lorem Ipsum is simply dummy text of the printing and typesetting industry. Lorem Ipsum has been the industry's standard dummy text ever since.</p>
  <div class="abs socials"><span class="on"></span><span></span><span></span><span></span><span></span></div>

  <h4 class="abs" style="right:79px;top:30px">USEFUL LINKS</h4>
  <ul class="abs links"><li>Privacy Policy</li><li>Terms &amp; Conditions</li><li>Sitemap</li></ul>

  <div class="abs copyright">©&nbsp;<i>Kelmora SERVICES</i>&nbsp;- 2016. All Rights Reserved.</div>
</footer>

</body>
</html>
```